Personal Injury Law Firm needs folder design

Need a folder design for our personal injury law firm, Horton & Quill, LLC. to give to all of our clients with their documents at the end of their case. I've attached our branding guide. We are branded as the 5 star law firm that fights for our clients like family. It should incorporate our colors or Green and White. We'd like to convey a message of moving on to the next chapter after finishing their case.

```html
<!DOCTYPE html>
<html lang="en">
<head>
<meta charset="utf-8">
<title>Horton &amp; Quill, LLC — Client Folder</title>
<link rel="stylesheet" href="https://fonts.googleapis.com/css2?family=Cinzel:wght@500&family=Open+Sans:wght@400;700&display=swap">
<style>
  :root {
    --bg: #f4f4f4;
    --green: #2f9e74;
    --green-deep: #2a8f69;
    --green-light: #34a87b;
    --ink: #1c3a40;
    --ink-deep: #183136;
    --paper: #ffffff;
    --text: #333333;
  }
  * { margin: 0; padding: 0; box-sizing: border-box; }
  html, body { width: 1200px; height: 1200px; overflow: hidden; background: var(--bg); }
  .canvas { position: relative; width: 1200px; height: 1200px; }

  /* Inside spread */
  .spread { position: absolute; left: 50px; top: 370px; width: 660px; height: 460px; display: flex; box-shadow: 0 14px 30px rgba(0,0,0,.12); }
  .panel { position: relative; width: 330px; height: 460px; overflow: hidden; }
  .panel--left { background: var(--green-deep); }
  .panel--right { background: var(--green); border-left: 1px solid rgba(0,0,0,.12); }

  .letter { position: absolute; left: 28px; top: 22px; width: 274px; height: 400px; background: var(--paper); padding: 20px 22px; font-family: "Open Sans", sans-serif; color: var(--text); }
  .letter__brand { display: flex; align-items: center; gap: 6px; margin-bottom: 22px; }
  .brand-square { width: 18px; height: 18px; background: var(--green); flex: none; }
  .letter__name { font-family: "Cinzel", serif; font-weight: 500; font-size: 10px; color: var(--green); letter-spacing: .04em; }
  .letter__heading { font-size: 7px; margin-bottom: 8px; }
  .letter__to { font-size: 6.5px; font-weight: 700; }
  .letter__addr { font-size: 5px; line-height: 1.4; margin-bottom: 12px; }
  .letter__para { font-size: 5.2px; line-height: 1.45; margin-bottom: 7px; }

  .pocket { position: absolute; left: 0; bottom: 0; width: 330px; height: 460px; }

  /* Front cover */
  .cover { position: absolute; left: 770px; top: 370px; width: 340px; height: 460px; background: var(--ink); box-shadow: 0 14px 30px rgba(0,0,0,.14); overflow: hidden; border-bottom: 4px solid var(--green); }
  .cover__pattern { position: absolute; inset: 0; background: linear-gradient(160deg, #25464c 0%, var(--ink) 45%, var(--ink-deep) 100%); }
  .cover__brand { position: absolute; left: 30px; top: 330px; display: flex; align-items: center; gap: 10px; }
  .cover__brand .brand-square { width: 40px; height: 40px; }
  .cover__name { font-family: "Cinzel", serif; font-weight: 500; font-size: 20px; color: var(--green-light); letter-spacing: .03em; }
</style>
</head>
<body>
<main class="canvas">
  <section class="spread">
    <div class="panel panel--left"></div>
    <div class="panel panel--right">
      <article class="letter">
        <header class="letter__brand">
          <span class="brand-square"></span>
          <span class="letter__name">Horton &amp; Quill, LLC</span>
        </header>
        <p class="letter__heading">Lorem ipsum</p>
        <p class="letter__to">Letter To:</p>
        <p class="letter__addr">Lorem ipsum dolor sit amet,<br>consectetuer adipiscing elit, sed</p>
        <p class="letter__para">Lorem ipsum dolor sit amet, consectetuer adipiscing elit, sed diam nonummy nibh euismod tincidunt ut laoreet dolore magna aliquam erat volutpat. Ut wisi enim ad minim veniam, quis nostrud exerci tation ullamcorper suscipit lobortis nisl ut aliquip ex ea commodo consequat.</p>
        <p class="letter__para">Lorem ipsum dolor sit amet, cons ectetuer adipiscing elit, sed diam nonummy nibh euismod tincidunt ut laoreet dolore magna aliquam erat volutpat.</p>
        <p class="letter__para">Lorem ipsum dolor sit amet, consectetuer adipiscing elit, sed diam nonummy nibh euismod tincidunt ut laoreet dolore magna aliquam erat volutpat. Duis autem vel eum iriure dolor in hendrerit.</p>
        <p class="letter__para">Lorem ipsum dolor sit amet, cons ectetuer adipiscing elit, sed diam euismod tincidunt ut laoreet dolore magna aliquam erat volutpat.</p>
      </article>
      <svg class="pocket" viewBox="0 0 330 460" aria-hidden="true">
        <path d="M0 260 Q0 250 12 252 L0 252 Z" fill="var(--green-light)"/>
        <path d="M0 250 L150 330 L330 170 L330 460 L0 460 Z" fill="var(--green-light)"/>
        <path d="M0 250 L150 330 L330 170" fill="none" stroke="rgba(0,0,0,.12)" stroke-width="1.5"/>
      </svg>
    </div>
  </section>

  <section class="cover">
    <div class="cover__pattern" role="img" aria-label="Faint geometric line pattern across the dark cover"></div>
    <div class="cover__brand">
      <span class="brand-square"></span>
      <span class="cover__name">Horton &amp; Quill, LLC</span>
    </div>
  </section>
</main>
</body>
</html>
```